Flyer-Design für Bed & Breakfast am Sorpesee
Zielgruppe
Wir haben ein Bed and Breakfast am Sorpesee in Sundern. Die Zimmer sind individuell, mit Liebe eingerichtet. Wir bieten ein außergewöhnliches Frühstück. Unsere Zielgruppe sind sportliche Menschen (Motorradfahrer, Radfahrer, Wanderer etc.) die hier rund um unser Haus ein außergewöhnlich gutes Angebot finden. Uns hebt ein großer Garten und ein einzigartiges Kamin/Grillzimmer von den üblichen Häusern ab.
Aufgabenstellung
So individuell wie unser Haus soll auch der Flyer sein. Weniger Text - mehr Emotionen durch Bilder. Bitte schon einmal die Bilder von der Homepage ansehen - diese werden noch durch ein zwei drei Gartenfotos ergänzt. Farben und Schriften sollten sich ebenfalls hieran orientieren.

```html
<!DOCTYPE html>
<html lang="de">
<head>
<meta charset="utf-8">
<title>Seehof Bed &amp; Breakfast – Zimmer</title>
<link href="https://fonts.googleapis.com/css2?family=Ubuntu:wght@400;500;700&display=swap" rel="stylesheet">
<style>
  :root {
    --page-bg: #e8e8e8;
    --sheet: #ffffff;
    --panel: #fdeab2;
    --ink: #b4965a;
    --ink-strong: #a8874a;
  }
  * { box-sizing: border-box; margin: 0; padding: 0; }
  html, body { width: 1200px; height: 866px; overflow: hidden; background: var(--page-bg); }
  body { font-family: "Ubuntu", sans-serif; color: var(--ink); position: relative; }

  .sheet { position: absolute; left: 43px; top: 42px; width: 1114px; height: 796px; background: var(--sheet); }

  .info-panel { position: absolute; left: 66px; top: 65px; width: 515px; height: 751px; }
  .info-panel svg.panel-shape { position: absolute; inset: 0; }

  .brand { position: absolute; left: 66px; top: 74px; display: flex; align-items: center; gap: 4px;
           font-size: 10px; font-weight: 700; color: var(--ink-strong); }
  .brand-dot { width: 9px; height: 9px; border-radius: 50%; background: var(--ink-strong); }

  .headline { position: absolute; left: 174px; top: 92px; width: 300px; text-align: center;
              font-size: 13.5px; font-weight: 700; color: var(--ink-strong); white-space: nowrap; }

  .intro { position: absolute; left: 113px; font-size: 12px; line-height: 13.2px;
           letter-spacing: 0.45px; white-space: nowrap; }
  .intro b { font-weight: 700; }
  .intro-1 { top: 123px; }
  .intro-2 { top: 204px; }
  .intro-3 { top: 298px; }

  .prices { position: absolute; left: 113px; top: 361px; font-size: 12px; line-height: 18.3px;
            letter-spacing: 0.4px; white-space: nowrap; }
  .room-prices + .room-prices { margin-top: 8px; }
  .room-prices h3 { font-size: 13px; font-weight: 700; color: var(--ink-strong); letter-spacing: 0.3px; }
  .room-prices .season { font-weight: 700; color: var(--ink-strong); }

  .photo { position: absolute; }
  .caption { position: absolute; font-size: 19.5px; font-weight: 400; color: var(--ink); text-align: center; width: 256px;
             letter-spacing: 0.5px; white-space: nowrap; }
</style>
</head>
<body>
  <div class="sheet"></div>

  <div class="info-panel">
    <svg class="panel-shape" width="515" height="751" viewBox="0 0 515 751">
      <polygon points="109,0 515,0 515,751 0,751 0,85" fill="var(--panel)"/>
    </svg>
  </div>

  <div class="brand"><span class="brand-dot"></span>Seehof</div>

  <h1 class="headline">Für jeden Geschmack das passende Zimmer</h1>

  <p class="intro intro-1">Rund um den Sorpesee im Sauerland dreht sich vieles um Freizeit und<br>Entspannung. Hier findet fast jeder genau das, was er sucht. Ob auf<br>einem der vielen Wanderpfade, mit Motorrad oder Rad auf kurvigen<br>Strecken, beim Golfen, Tauchen, Schwimmen oder auf Skiern,<br>und vieles mehr...</p>

  <p class="intro intro-2">Auch bei uns im Haus gibt es viele Wege zum Abschalten. Allen voran<br>unser großer Garten mit 5000 qm, der sowohl ruhige Plätze mit<br>Liegen und Gartenstühlen als auch eine vollständig umzäunte<br>Freifläche für unsere vierbeinigen Besucher bereithält. Eine<br>Feuerstelle, die wir auf Wunsch gerne für Sie anzünden, gehört<br>natürlich ebenfalls dazu.</p>

  <p class="intro intro-3">Jedes Zimmer ist mit einem <b>Fernseher</b> und kostenlosem <b>W-Lan</b><br>ausgestattet, Handtücher liegen bereit und im Bad gibt es <b>Shampoo</b><br>sowie einen Föhn! Auch besondere Wünsche erfüllen wir gern!</p>

  <div class="prices">
    <section class="room-prices">
      <h3>Midnight ride Kosten:</h3>
      <p class="season">01.04. – 31.10.</p>
      <p>EUR 60,00 pro Nacht inkl. Frühstück</p>
      <p>Kurzbucherzuschlag am Wochenende für nur eine Nacht EUR 20,00</p>
      <p class="season">01.11. – 31.03.</p>
      <p>EUR 50,00 pro Nacht inkl. Frühstück</p>
      <p>Aufpreis bei Nutzung als Doppelzimmer EUR 15,00 pro Person und Nacht</p>
    </section>
    <section class="room-prices">
      <h3>Fresh fern Kosten:</h3>
      <p class="season">01.04. – 31.10.</p>
      <p>EUR 90,00 pro Nacht inkl. Frühstück für zwei Personen</p>
      <p>Kurzbucherzuschlag am Wochenende für nur eine Nacht EUR 20,00</p>
      <p class="season">01.11. – 31.03.</p>
      <p>EUR 80,00 pro Nacht inkl. Frühstück für zwei Personen</p>
      <p>Aufpreis Hund EUR 10,00 pro Aufenthalt</p>
    </section>
    <section class="room-prices">
      <h3>Moon glow Kosten:</h3>
      <p class="season">01.04. – 31.10.</p>
      <p>EUR 110,00 pro Nacht inkl. Frühstück für zwei Personen</p>
      <p>Kurzbucherzuschlag am Wochenende für nur eine Nacht EUR 20,00</p>
      <p class="season">01.11. – 31.03.</p>
      <p>EUR 100,00 pro Nacht inkl. Frühstück für zwei Personen</p>
      <p>Aufpreis Hund EUR 10,00 pro Aufenthalt</p>
      <p>Aufpreis 3. Begleitperson ab 14 Jahren EUR 20,00 pro Nacht (unser</p>
      <p>Haus ist nicht für Kinder unter 14 Jahren geeignet)</p>
    </section>
  </div>

  <div class="photo" role="img" aria-label="Zimmer mit dunkelblauer Wand, beleuchteten Fahrradfelgen, Lederbank und Fell auf Parkett"
       style="left:619px;top:65px;width:255px;height:340px;background:linear-gradient(160deg,#e6dccb 0%,#2c3f66 40%,#3a4263 55%,#b07a3a 80%,#8a5a2a 100%);"></div>
  <div class="photo" role="img" aria-label="Gastgeberin bereitet Obst auf einer Etagere für das Frühstück auf der Terrasse vor"
       style="left:893px;top:65px;width:241px;height:156px;background:linear-gradient(120deg,#c9d0c2 0%,#8e9a80 40%,#b56068 65%,#1e1e22 100%);"></div>
  <div class="photo" role="img" aria-label="Zimmer mit grüner Wand, Bücherregal, Sessel und Kissen"
       style="left:893px;top:248px;width:241px;height:157px;background:linear-gradient(100deg,#d8d5c6 0%,#ece9dc 45%,#b8bf72 75%,#8c9a3c 100%);"></div>
  <div class="photo" role="img" aria-label="Großer Garten mit Rasen, Bäumen und Blick über die Hügel"
       style="left:619px;top:441px;width:255px;height:181px;background:linear-gradient(180deg,#7fb2e6 0%,#c6dcee 35%,#4f7a3a 55%,#2f5222 70%,#6a9a36 100%);"></div>
  <div class="photo" role="img" aria-label="Zimmer mit dunkler Wand, Doppelbett mit blauer Decke und roten Kissen"
       style="left:893px;top:441px;width:241px;height:181px;background:linear-gradient(170deg,#2a2a30 0%,#3b3b44 45%,#7a7fae 65%,#c08a44 100%);"></div>
  <div class="photo" role="img" aria-label="Kamin- und Grillzimmer mit offenem Kamin, Holzbalken und roter Bank"
       style="left:619px;top:657px;width:255px;height:159px;background:linear-gradient(160deg,#3a2a22 0%,#a9a08e 40%,#d8cbb4 60%,#b8322e 85%,#5a2a22 100%);"></div>
  <div class="photo" role="img" aria-label="Heller Wohnraum mit Hängesessel vor großen Fenstern und Teppich auf Parkett"
       style="left:893px;top:657px;width:241px;height:159px;background:linear-gradient(170deg,#e4e6e0 0%,#a8b89a 35%,#8a8a8c 60%,#b98a50 100%);"></div>

  <p class="caption" style="left:614px;top:408px;">Midnight ride</p>
  <p class="caption" style="left:896px;top:409px;">Fresh fern</p>
  <p class="caption" style="left:614px;top:624px;">Der Garten</p>
  <p class="caption" style="left:896px;top:625px;">Moon glow</p>
</body>
</html>
```